Ridgeline Talent Associates Business Card Design

We need a business card design for our new company - Ridgeline Talent Associates. RLTA is a recruitment firm that focuses on recruiting engineers and geologist for mid-size oil and gas companies. We would like our logo on the business card, which is attached, and we would like the color scheme on business cards to coordinate with our logo.

Industry/Entity Type

Oil And Gas

Contact Information for Business Card

Dana Whitlow, Founder and Managing Partner, dmw@ridgelinetalentco.org, 888.507.3942 (work), 5730915.0600 (cell), 573.642.1907 (fax), www.ridgelinetalentco.org

```html
<!DOCTYPE html>
<html lang="en">
<head>
<meta charset="utf-8">
<title>Ridgeline Talent Associates – Business Card</title>
<link href="https://fonts.googleapis.com/css2?family=Open+Sans:wght@400;600&display=swap" rel="stylesheet">
<style>
  :root {
    --navy: #35356a;
    --navy-deep: #2c2c5c;
    --sweep-grey: #a7a8b0;
    --paper: #ffffff;
    --backdrop: #e6e6ea;
    --soft-text: #d9d9ea;
  }
  * { box-sizing: border-box; margin: 0; padding: 0; }
  html, body {
    width: 1200px; height: 900px; overflow: hidden;
    background: var(--backdrop);
    font-family: "Open Sans", Arial, sans-serif;
  }
  .canvas {
    position: relative; width: 1200px; height: 900px;
  }
  .card {
    position: absolute; left: 270px;
    width: 660px; height: 377px;
    border-radius: 38px; overflow: hidden;
    background: var(--paper);
    box-shadow: 0 6px 22px rgba(40, 40, 70, 0.16);
  }
  .card-front { top: 50px; }
  .card-back { top: 473px; }
  .card-shape { position: absolute; inset: 0; }
  .holder {
    position: absolute; left: 34px; top: 30px;
    color: var(--paper);
  }
  .holder-name { font-size: 23px; font-weight: 600; letter-spacing: 0.2px; }
  .holder-title { font-size: 15px; color: var(--soft-text); margin-top: 2px; }
  .contact-list {
    position: absolute; left: 34px; top: 196px;
    list-style: none; color: var(--paper); font-size: 14px;
  }
  .contact-item { display: flex; align-items: center; gap: 10px; height: 27px; }
  .contact-icon {
    width: 18px; height: 18px; border-radius: 50%;
    background: var(--paper);
    display: flex; align-items: center; justify-content: center;
  }
  .contact-icon svg { width: 11px; height: 11px; fill: var(--navy); }
  .brand {
    position: absolute; display: flex; align-items: center; gap: 12px;
    color: var(--navy);
  }
  .brand-dot {
    width: 30px; height: 30px; border-radius: 50%;
    background: var(--navy); flex: none;
  }
  .brand-name {
    font-size: 19px; font-weight: 600; letter-spacing: 1.2px;
    text-transform: uppercase; line-height: 1.15;
  }
  .card-front .brand { left: 352px; top: 162px; width: 280px; }
  .card-back .brand { left: 50%; top: 50%; transform: translate(-50%, -50%); width: 320px; }
</style>
</head>
<body>
<main class="canvas">

  <section class="card card-front" aria-label="Business card front">
    <svg class="card-shape" viewBox="0 0 660 377" preserveAspectRatio="none" aria-hidden="true">
      <path d="M0 0 H342 C268 70 250 300 305 377 H0 Z" fill="var(--sweep-grey)"/>
      <path d="M0 0 H310 C240 70 222 300 272 377 H0 Z" fill="var(--navy)"/>
    </svg>

    <div class="holder">
      <p class="holder-name">Dana Whitlow</p>
      <p class="holder-title">Director</p>
    </div>

    <ul class="contact-list">
      <li class="contact-item">
        <span class="contact-icon"><svg viewBox="0 0 24 24"><path d="M6.6 10.8a15.1 15.1 0 0 0 6.6 6.6l2.2-2.2a1 1 0 0 1 1-.25 11.4 11.4 0 0 0 3.6.57 1 1 0 0 1 1 1V20a1 1 0 0 1-1 1A17 17 0 0 1 3 4a1 1 0 0 1 1-1h3.5a1 1 0 0 1 1 1c0 1.25.2 2.45.57 3.57a1 1 0 0 1-.25 1z"/></svg></span>
        888.507.3942
      </li>
      <li class="contact-item">
        <span class="contact-icon"><svg viewBox="0 0 24 24"><path d="M7 1h10a2 2 0 0 1 2 2v18a2 2 0 0 1-2 2H7a2 2 0 0 1-2-2V3a2 2 0 0 1 2-2zm0 4v13h10V5zm5 14.5a1 1 0 1 0 0 2 1 1 0 0 0 0-2z"/></svg></span>
        5730915.0600
      </li>
      <li class="contact-item">
        <span class="contact-icon"><svg viewBox="0 0 24 24"><path d="M2 5h20v14H2zm2 2v.4l8 5 8-5V7zm0 2.8V17h16V9.8l-8 5z"/></svg></span>
        dmw@ridgelinetalentco.org
      </li>
    </ul>

    <div class="brand">
      <span class="brand-dot"></span>
      <span class="brand-name">Ridgeline Talent Associates</span>
    </div>
  </section>

  <section class="card card-back" aria-label="Business card back">
    <div class="brand">
      <span class="brand-dot"></span>
      <span class="brand-name">Ridgeline Talent Associates</span>
    </div>
  </section>

</main>
</body>
</html>
```